Morvel & Morvel**

Liquid Mega-Mag (400 mg) 4 oz
Liquid Ionic B12 (1,000 mcg) 2 oz
Probiotic 55 Billion 30 CT
Liquid Potassium 99mg
Liquid Iodide 225mcg
Liquid Strontium 100 mg
Liquid Iron 22mg
Liquid Ionic Zinc (50 mg) 2 oz
Liquid Ionic Selenium (300 mcg) 2 oz
Lonic Boron 6 mg
Fulvic Acid 250 mg
Chromium 550 mcg
Ox Bile 500 mg
Vitamin D3 1000 IU
Liver Support 1000 IU
Tonify blood 1000 IU
Adrenal Support 1000 IU
Constipation 1000 IU

Target Market(s)

public

Industry/Entity Type

Health And Wellness

Font styles to use
Serif

Requirements
Must have
• color
Nice to have
• I would like to see the designer's views.
Should not have
• I don't have any

```html
<!DOCTYPE html>
<html lang="en">
<head>
<meta charset="utf-8">
<title>Morvel &amp; Morvel Supplement Label</title>
<link rel="stylesheet" href="https://fonts.googleapis.com/css2?family=Tinos:wght@400;700&family=Archivo+Narrow:wght@500;600&display=swap">
<style>
  :root {
    --backdrop: #dcdcda;
    --label: #ffffff;
    --ink-purple: #3a1a6e;
    --ink-violet: #5b2a9a;
    --ink-red: #d9162e;
    --ink-crimson: #b3123c;
    --pill-red: #e01b2c;
    --pill-purple: #40266c;
    --mark: #c2173a;
  }
  * { margin: 0; padding: 0; box-sizing: border-box; }
  html, body {
    width: 1200px;
    height: 900px;
    overflow: hidden;
    background: var(--backdrop);
  }
  .canvas {
    width: 1200px;
    height: 900px;
    display: flex;
    align-items: center;
    justify-content: center;
  }
  .label {
    width: 720px;
    height: 700px;
    background: var(--label);
    border-radius: 18px;
    display: flex;
    flex-direction: column;
    align-items: center;
    padding-top: 56px;
    font-family: "Tinos", "Times New Roman", serif;
  }
  .brand-mark {
    width: 200px;
    height: 200px;
    border-radius: 50%;
    background: var(--mark);
  }
  .brand-name {
    margin-top: 22px;
    font-weight: 700;
    font-size: 52px;
    color: var(--ink-purple);
    letter-spacing: 1px;
    line-height: 1;
  }
  .brand-rule {
    width: 330px;
    height: 2px;
    background: var(--ink-purple);
    margin-top: 10px;
  }
  .product-title {
    margin-top: 14px;
    font-weight: 700;
    font-size: 104px;
    line-height: 1;
    letter-spacing: 1px;
    background: linear-gradient(90deg, var(--ink-violet) 0%, var(--ink-red) 45%, var(--ink-red) 70%, var(--ink-violet) 100%);
    -webkit-background-clip: text;
    background-clip: text;
    color: transparent;
  }
  .tagline {
    margin-top: 18px;
    font-weight: 700;
    font-size: 30px;
    line-height: 1.3;
    color: var(--ink-crimson);
    text-align: center;
    letter-spacing: 0.5px;
  }
  .badges {
    margin-top: 30px;
    display: flex;
    font-family: "Archivo Narrow", "Arial Narrow", sans-serif;
    font-weight: 600;
    font-size: 24px;
    color: #ffffff;
    letter-spacing: 0.5px;
  }
  .badge {
    padding: 8px 26px;
    line-height: 1.1;
  }
  .badge-count {
    background: var(--pill-red);
    border-radius: 24px 0 0 24px;
  }
  .badge-type {
    background: var(--pill-purple);
    border-radius: 0 24px 24px 0;
  }
</style>
</head>
<body>
  <main class="canvas">
    <section class="label">
      <div class="brand-mark" aria-hidden="true"></div>
      <h1 class="brand-name">Morvel &amp; Morvel</h1>
      <div class="brand-rule"></div>
      <h2 class="product-title">SUPPLEMENT</h2>
      <p class="tagline">All-Natural and Safe<br>Supplement for Body Health</p>
      <div class="badges">
        <span class="badge badge-count">60 CAPSULES</span>
        <span class="badge badge-type">DIETARY SUPPLEMENT</span>
      </div>
    </section>
  </main>
</body>
</html>
```